We are a General Practice - Family medicine
We also have Allied Health professionals working within our team

Industry/Entity Type

Business

Contact Information for Business Card

Front of the card to display:

HARBOURVIEW MEDICAL
PHONE 6381 2947

5/14 Kellerton Avenue
Launceston Tasmania 7268

Back of the card to display:

My Appointments
Date:
Time:
With:

Please remember to phone us on 6381 2947 to cancel your appointment if you can't keep it.
A fee applied to missed appointments

```html
<!DOCTYPE html>
<html lang="en">
<head>
<meta charset="utf-8">
<title>Harbourview Medical – Business Card</title>
<link rel="stylesheet" href="https://fonts.googleapis.com/css2?family=Lato:wght@400;700;900&display=swap">
<style>
  :root {
    --blue: #17a5e3;
    --green: #8cc63f;
    --grey: #7a7d80;
    --ink: #5c5f62;
    --paper: #ffffff;
    --backdrop: #e4e5e7;
  }
  * { box-sizing: border-box; margin: 0; padding: 0; }
  html, body {
    width: 1200px; height: 913px; overflow: hidden;
    background: var(--backdrop);
    font-family: "Lato", Arial, sans-serif;
  }
  .sheet {
    width: 1200px; height: 913px;
    display: flex; justify-content: center; align-items: center; gap: 70px;
  }
  .card {
    position: relative;
    width: 370px; height: 572px;
    background: var(--paper);
    box-shadow: 0 4px 18px rgba(0,0,0,.12);
    display: flex; flex-direction: column; align-items: center;
    padding-top: 52px;
  }
  .card__band {
    position: absolute; left: 0; right: 0; bottom: 0; height: 32px;
    background: var(--blue);
    border-top: 6px solid var(--green);
  }
  .brand__dot {
    width: 78px; height: 78px; border-radius: 50%;
    background: var(--green);
  }
  .brand__name {
    margin-top: 16px;
    font-size: 36px; font-weight: 400; color: var(--blue);
    letter-spacing: -0.3px;
  }
  .brand__sub {
    margin-top: 12px;
    font-size: 12px; color: var(--grey); letter-spacing: 3.4px;
  }
  .front .brand__title {
    margin-top: 26px;
    font-size: 17px; font-weight: 900; color: var(--blue); letter-spacing: 1px;
  }
  .contact { align-self: stretch; padding: 0 34px; margin-top: 44px; }
  .contact__row { display: flex; align-items: center; gap: 20px; margin-bottom: 30px; }
  .contact__icon {
    width: 52px; height: 52px; border-radius: 4px; background: var(--blue);
    display: flex; align-items: center; justify-content: center; flex-shrink: 0;
  }
  .contact__phone { font-size: 22px; color: var(--ink); letter-spacing: 1px; }
  .contact__address { font-size: 14px; color: var(--grey); line-height: 1.5; letter-spacing: .6px; }
  .front .tagline {
    margin-top: 12px;
    font-size: 14px; font-weight: 900; color: var(--blue); letter-spacing: .4px;
  }
  .back { padding-top: 30px; }
  .back .brand__dot { width: 60px; height: 60px; }
  .back .brand__name { margin-top: 10px; font-size: 34px; }
  .back .brand__sub { margin-top: 8px; font-size: 11px; }
  .back .brand__title {
    margin-top: 10px;
    font-size: 15px; font-weight: 900; color: var(--green); letter-spacing: .8px;
  }
  .ribbon { margin-top: 12px; width: 260px; height: 42px; position: relative; }
  .ribbon svg { display: block; }
  .ribbon span {
    position: absolute; inset: 0; display: flex; align-items: center; justify-content: center;
    color: #fff; font-weight: 900; font-size: 19px; letter-spacing: 1.6px;
  }
  .fields { align-self: stretch; padding: 0 34px 0 44px; margin-top: 12px; }
  .field { margin-bottom: 6px; }
  .field__label { font-size: 14px; line-height: 1.2; color: var(--ink); letter-spacing: .5px; }
  .field__box { margin-top: 2px; height: 22px; border: 2px dashed var(--blue); border-radius: 2px; }
  .notice {
    margin-top: 12px; text-align: center;
    font-size: 13px; font-weight: 900; color: var(--green);
    font-variant: small-caps; line-height: 1.3; letter-spacing: .5px;
  }
  .notice strong { color: var(--blue); font-variant: normal; font-size: 14px; }
  .notice__fee { color: var(--blue); }
</style>
</head>
<body>
<main class="sheet">

  <section class="card front" aria-label="Card front">
    <div class="brand__dot"></div>
    <h1 class="brand__name">Harbourview Medical</h1>
    <p class="brand__sub">HEALTHCARE CENTRE</p>
    <p class="brand__title">HARBOURVIEW MEDICAL</p>

    <div class="contact">
      <div class="contact__row">
        <div class="contact__icon">
          <svg width="30" height="30" viewBox="0 0 24 24" aria-hidden="true">
            <path fill="#fff" d="M6.6 10.8a15.1 15.1 0 0 0 6.6 6.6l2.2-2.2c.3-.3.7-.4 1-.2 1.1.4 2.3.6 3.6.6.6 0 1 .4 1 1V20c0 .6-.4 1-1 1A17 17 0 0 1 3 4c0-.6.4-1 1-1h3.5c.6 0 1 .4 1 1 0 1.3.2 2.5.6 3.6.1.3 0 .7-.2 1z"/>
          </svg>
        </div>
        <span class="contact__phone">6381 2947</span>
      </div>
      <div class="contact__row">
        <div class="contact__icon">
          <svg width="32" height="32" viewBox="0 0 24 24" aria-hidden="true">
            <path fill="none" stroke="#fff" stroke-width="1.8" d="M12 3a4.5 4.5 0 0 0-4.5 4.5c0 3.4 4.5 8 4.5 8s4.5-4.6 4.5-8A4.5 4.5 0 0 0 12 3z"/>
            <circle cx="12" cy="7.5" r="1.6" fill="#fff"/>
            <path fill="none" stroke="#fff" stroke-width="1.8" d="M7 14H4l-1.5 6h19L20 14h-3"/>
          </svg>
        </div>
        <p class="contact__address">5/14 Kellerton Avenue<br>Launceston Tasmania 7268</p>
      </div>
    </div>

    <p class="tagline">FOR BEETER LIFE AND GOOD HELTH</p>
    <div class="card__band"></div>
  </section>

  <section class="card back" aria-label="Card back">
    <div class="brand__dot"></div>
    <h2 class="brand__name">Harbourview Medical</h2>
    <p class="brand__sub">HEALTHCARE CENTRE</p>
    <p class="brand__title">HARBOURVIEW MEDICAL</p>

    <div class="ribbon">
      <svg width="260" height="42" viewBox="0 0 260 42" aria-hidden="true">
        <path fill="var(--blue)" d="M0 3 H260 L248 21 L260 39 H0 L12 21 Z"/>
      </svg>
      <span>MY APOINTMENT</span>
    </div>

    <div class="fields">
      <div class="field"><p class="field__label">Date</p><div class="field__box"></div></div>
      <div class="field"><p class="field__label">Time</p><div class="field__box"></div></div>
      <div class="field"><p class="field__label">With</p><div class="field__box"></div></div>
    </div>

    <p class="notice">
      Please remember to phone us on<br>
      <strong>6381 2947</strong> to cancel your appointment<br>
      if you can't keep it.<br>
      <span class="notice__fee">A fee applied to missed appointments</span>
    </p>
    <div class="card__band"></div>
  </section>

</main>
</body>
</html>
```